Smart Home App Needs 4 Mockup Screens. Extra Work Guaranteed for Winner

BACKGROUND
Our company, Marlow, is launching an exciting new app early next year. And we need some examples of what our app will look like to show to some of the biggest retailers in the world. We hope that this project will lead to regular work as we have a lot of new products planned for the app.

Our app will support baby, home and pet monitors (cameras) as well as the world's first smart pet flap.

The monitors allow you to do much more than just watch live video. By monitoring and providing information on sound, movement and temperature the app provides the user with instant peace of mind wherever they are. If anything has changed the user can be alerted via notifications. If motion is detected the user will receive a clip of the whole event moments after it has happened.

The Smart Pet Flap is packed full of features too. From letting you decide when your pet can or can't go outside from your mobile, to automatically opening if a fire is detected (along with a whole host of other features) - this really is the most advanced pet flap in the world.

REQUIREMENTS
We need 4 mock-up screens creating to show the UI of our app.
1. Camera Home Page
2. Camera Notifications Page
3. Pet Flap Fire Alarm Warning Page
4. Extreme Weather Warning Page

Optional - Happy to Pay the Winner Extra for these Designs
5. Start Up/Log In Page
6. Pet Flap Notification Example
7. Pet Flap Scheduler Page (your choice)
(SEE MARLOW APP DESIGN COMPETITION - ATTACHED)

STYLE GUIDE
As you'll see from our wireframes we want our app to be very minimal and modern. The predominant colour will be white but where colour is used it should be bright (see our colour palette - which we will provide shortly).

INSPIRATION
We love the UI of Tumbleweed (home surveillance). Also check out Pike (smart thermostat).
(SEE MARLOW UI EXAMPLES ATTACHED)

LOGO
We love our logo. Feel free to use it in creative ways.

So far we're also using it as a kind of beacon to indicate if everything is ok.

LOGO COLOURS & APP COLOURS
As mentioned, we are thinking of using the green logo to indicate that everything is ok (and also for the pet app in general). We reserve red for when something has happened (normally bad) and needs attention, like a fire alarm going off.

The app will be predominantly black and white with the odd minimal flash of colour (probably primary colour)
We'll upload a colour scheme as soon as we have it.

CONTACT
Please message us for more details - we'll do our best to reply promptly.

FUTURE WORK
We will need extra screens made straight after the competition is over and there should be additional regular work after this.

Target Market(s)

Our app will be used by young professionals, to young parents to grandparents. The design must be contemporary but timeless and easy to use no matter how good you are with technology.

Industry/Entity Type

Pet

Font styles to use
Sans Serif

Colors
faee3f
33a6d7
ec1f27
acd036
32b7a4

Requirements
Must have
• Beautiful, minimal design. Make sure you spend time looking at the Tumbleweed and Pike apps before starting.

For the videos make sure you use sensible images - that you'd expect to see from a monitor (high resolution images if possible)
Nice to have
• Creative use of our logo.
Should not have
• Too much detail/clutter/colours. Ugly fonts.

```html
<!DOCTYPE html>
<html lang="en">
<head>
<meta charset="utf-8">
<title>Marlow – Severe Weather Lock Screen Alert</title>
<link href="https://fonts.googleapis.com/css2?family=Roboto:wght@100;300;400&display=swap" rel="stylesheet">
<style>
  :root {
    --bg-top: #162227;
    --bg-mid: #41474a;
    --bg-bottom: #1e2a2f;
    --text: #ffffff;
    --text-soft: rgba(255, 255, 255, 0.82);
    --text-faint: rgba(255, 255, 255, 0.28);
    --chrome: rgba(255, 255, 255, 0.55);
    --bolt: #faee3f;
    --lens: #2a3438;
  }
  * { margin: 0; padding: 0; box-sizing: border-box; }
  html, body {
    width: 676px;
    height: 1200px;
    overflow: hidden;
    background: var(--bg-bottom);
  }
  .lock-screen {
    position: relative;
    width: 676px;
    height: 1200px;
    overflow: hidden;
    font-family: "Roboto", sans-serif;
    color: var(--text);
  }
  .wallpaper {
    position: absolute;
    inset: 0;
    background: linear-gradient(180deg, var(--bg-top) 0%, var(--bg-mid) 55%, var(--bg-bottom) 100%);
  }
  .status-bar {
    position: absolute;
    top: 0; left: 0; right: 0;
    height: 52px;
  }
  .signal {
    position: absolute;
    left: 15px; top: 19px;
    display: flex;
    gap: 3px;
  }
  .signal span {
    width: 13px; height: 13px;
    border-radius: 50%;
    border: 1.5px solid var(--chrome);
  }
  .signal span.on { background: var(--chrome); border-color: transparent; }
  .carrier {
    position: absolute;
    left: 106px; top: 10px;
    font-size: 27px;
    font-weight: 300;
    color: var(--chrome);
  }
  .wifi { position: absolute; left: 192px; top: 14px; }
  .battery-level {
    position: absolute;
    right: 81px; top: 10px;
    font-size: 27px;
    font-weight: 300;
    color: var(--chrome);
  }
  .battery { position: absolute; right: 14px; top: 15px; }
  .grabber {
    position: absolute;
    left: 301px;
    width: 74px; height: 14px;
    border-radius: 7px;
    background: rgba(255,255,255,0.28);
  }
  .grabber.top { top: 19px; }
  .grabber.bottom { top: 1165px; }
  .clock {
    position: absolute;
    top: 90px; left: 0; right: 0;
    text-align: center;
    font-size: 180px;
    font-weight: 100;
    line-height: 1;
    letter-spacing: -4px;
  }
  .date {
    position: absolute;
    top: 266px; left: 0; right: 0;
    text-align: center;
    font-size: 39px;
    font-weight: 300;
  }
  .notification {
    position: absolute;
    top: 408px; left: 19px; right: 20px;
    display: flex;
    gap: 18px;
  }
  .notification-icon { flex: none; margin-top: 16px; }
  .notification-app {
    font-size: 19px;
    font-weight: 300;
    color: var(--text-soft);
    line-height: 24px;
  }
  .notification-title,
  .notification-body {
    font-size: 31px;
    font-weight: 300;
    line-height: 33px;
  }
  .notification-title { margin-top: 4px; }
  .notification-time {
    font-size: 20px;
    color: var(--text-soft);
  }
  .notification-hint {
    margin-top: 6px;
    font-size: 17px;
    font-weight: 300;
    color: var(--text-soft);
  }
  .unlock {
    position: absolute;
    top: 1000px; left: 135px;
    display: flex;
    align-items: center;
    gap: 25px;
    font-size: 52px;
    font-weight: 300;
    color: var(--text-faint);
  }
  .camera-shortcut { position: absolute; left: 603px; top: 1141px; }
</style>
</head>
<body>
<main class="lock-screen">
  <div class="wallpaper" role="img" aria-label="Wallpaper photo of a calm dark sea at dusk"></div>

  <header class="status-bar">
    <div class="signal"><span class="on"></span><span class="on"></span><span class="on"></span><span></span><span></span></div>
    <div class="carrier">Vantel</div>
    <svg class="wifi" width="30" height="22" viewBox="0 0 30 22" fill="none" stroke="rgba(255,255,255,0.55)" stroke-width="3" stroke-linecap="round">
      <path d="M3 8 a17 17 0 0 1 24 0"/>
      <path d="M8 13 a10 10 0 0 1 14 0"/>
      <circle cx="15" cy="18" r="2" fill="rgba(255,255,255,0.55)" stroke="none"/>
    </svg>
    <div class="grabber top"></div>
    <div class="battery-level">49%</div>
    <svg class="battery" width="58" height="24" viewBox="0 0 58 24">
      <rect x="1" y="1" width="50" height="22" rx="2" fill="none" stroke="rgba(255,255,255,0.55)" stroke-width="2"/>
      <rect x="4" y="4" width="23" height="16" fill="rgba(255,255,255,0.55)"/>
      <rect x="53" y="8" width="4" height="8" rx="1" fill="rgba(255,255,255,0.55)"/>
    </svg>
  </header>

  <div class="clock">7:21</div>
  <div class="date">Thursday, October 31</div>

  <section class="notification">
    <svg class="notification-icon" width="72" height="68" viewBox="0 0 72 68" fill="none">
      <path d="M16 44 h38 a12 12 0 0 0 0-24 a16 16 0 0 0-30-4 a12 12 0 0 0-8 28 z" stroke="#fff" stroke-width="4" stroke-linejoin="round"/>
      <path d="M40 30 l-8 14 h8 l-5 14 l14-18 h-8 l6-10 z" fill="var(--bolt)"/>
      <g stroke="#fff" stroke-width="3.5" stroke-linecap="round">
        <line x1="24" y1="50" x2="22" y2="56"/>
        <line x1="30" y1="52" x2="28" y2="58"/>
        <line x1="52" y1="50" x2="50" y2="56"/>
      </g>
    </svg>
    <div class="notification-text">
      <div class="notification-app">Marlow</div>
      <div class="notification-title">Severe Thunderstorm Warning!</div>
      <div class="notification-body">Rex is currently outside. <span class="notification-time">16m ago.</span></div>
      <div class="notification-hint">Slide to view</div>
    </div>
  </section>

  <div class="unlock">
    <svg width="22" height="44" viewBox="0 0 22 44" fill="none" stroke="rgba(255,255,255,0.28)" stroke-width="3">
      <path d="M3 2 L19 22 L3 42"/>
    </svg>
    <span>slide to unlock</span>
  </div>

  <div class="grabber bottom"></div>
  <svg class="camera-shortcut" width="58" height="42" viewBox="0 0 58 42">
    <path d="M4 8 h14 l5-6 h12 l5 6 h14 v32 h-50 z" fill="rgba(255,255,255,0.35)"/>
    <circle cx="29" cy="24" r="10" fill="none" stroke="var(--lens)" stroke-width="4"/>
  </svg>
</main>
</body>
</html>
```